Buch-/eBook-Cover für Elternratgeber
Zielgruppe
Titel des Buches: Der Mutkompass - Sieben Schritte zu innerer Ruhe im Familienalltag mit Schulanfängern
Dies ist ein Elternratgeber, der praktische und alltagstaugliche Tipps bietet, wie Eltern das Selbstbewusstsein ihrer Kinder fördern können, um sie für Herausforderungen der Welt zu stärken. Der Fokus liegt auf klaren, inspiererenden und leicht umzusetzenden Methoden.
Das Buch wird im Eigenverlag gedruckt. Als Designer haben sie die Freiheit, Ihre Kreativität einzusetzten, um ein ansprechendes Design zu gestalten, das die Zielgruppe anspricht (Eltern von Kindern von 4-12 Jahren)
Aufgabenstellung
Kein Comicstil: Der Stil sollte seriös und professionell wirken
Minimalistisch: Weniger ist mehr - ein aufgeräumtes und modernes Design wird bevorzugt
Inspirationsquelle: Orientieren sie sich gerne an erfolgreichen Elternratgebern auf Lesotrek, die hohe Bewertungen erhalten haben
Farben und Elemente: Keine festen Vorgaben, aber das Design sollte Vertrauen, Klarheit und Stärke strahlen.
Nachtrag:
Cover: für Softcover
Gerne bunt. Habe schon einige bekommen die gut sind. Manche sehen eher aus wie Fachbücher für Ärzte. Gerne kreativ.

```html
<!DOCTYPE html>
<html lang="de">
<head>
<meta charset="utf-8">
<title>Der Mutkompass – Buchumschlag</title>
<link rel="stylesheet" href="https://fonts.googleapis.com/css2?family=Anton&family=Oswald:wght@400;500&family=Roboto:wght@400&display=swap">
<style>
  :root {
    --navy: #1e3163;
    --back-bg: #e3e8fb;
    --front-light: #eceef9;
    --front-mid: #d6dbf0;
    --photo-skin: #c9a98f;
    --photo-shirt: #9a9aa2;
    --card: #c9a57e;
    --card-dark: #b89068;
    --badge-red: #a4140e;
    --white: #ffffff;
  }
  * { margin: 0; padding: 0; box-sizing: border-box; }
  html, body { width: 1200px; height: 800px; overflow: hidden; background: var(--white); }
  .canvas { position: relative; width: 1200px; height: 800px; }

  .cover { position: absolute; left: 20px; top: 18px; width: 1160px; height: 767px; display: flex; }

  /* Rückseite */
  .back-cover { width: 541px; height: 100%; background: var(--back-bg); padding: 68px 0 0 32px; }
  .back-title { font-family: "Anton", sans-serif; font-weight: 400; font-size: 26px; color: var(--navy); letter-spacing: 0.2px; }
  .back-blurb { margin-top: 14px; width: 480px; font-family: "Roboto", sans-serif; font-size: 17.2px; line-height: 24px; color: var(--navy); }

  /* Buchrücken */
  .spine { position: relative; width: 78px; height: 100%; background: var(--navy); }
  .spine-text {
    position: absolute; left: 50%; top: 50%;
    transform: translate(-50%, -50%) rotate(-90deg);
    white-space: nowrap; font-family: "Oswald", sans-serif; font-size: 25px;
    color: var(--white); letter-spacing: 0.3px;
    margin-top: -66px;
  }
  .spine-text .spine-author { margin-right: 26px; }

  /* Vorderseite */
  .front-cover { position: relative; flex: 1; height: 100%; overflow: hidden;
    background: linear-gradient(160deg, var(--front-light) 0%, var(--front-mid) 100%); }
  .photo-child {
    position: absolute; left: 100px; top: 380px; width: 320px; height: 387px;
    background: radial-gradient(ellipse at 55% 55%, var(--photo-skin) 0%, rgba(201,169,143,0.55) 38%, rgba(154,154,162,0.45) 70%, rgba(214,219,240,0) 100%);
  }
  .front-author { position: absolute; top: 22px; left: 0; right: 0; text-align: center;
    font-family: "Oswald", sans-serif; font-size: 31px; color: var(--navy); }
  .front-title { position: absolute; top: 70px; left: 0; right: 0; display: flex; flex-direction: column; align-items: center;
    font-family: "Anton", sans-serif; color: var(--navy); text-transform: uppercase; line-height: 1; }
  .title-row { display: flex; align-items: center; }
  .title-small { display: flex; flex-direction: column; font-size: 31px; line-height: 0.98; margin-right: 10px; text-align: center; }
  .title-big { font-size: 96px; line-height: 1.02; letter-spacing: 0.5px; }

  .sign { position: absolute; left: 118px; top: 330px; width: 316px; height: 160px;
    background: linear-gradient(170deg, var(--card) 0%, var(--card-dark) 100%);
    transform: rotate(3deg); display: flex; align-items: center; justify-content: center; }
  .sign-text { font-family: "Anton", sans-serif; font-size: 47px; line-height: 1.08; color: var(--navy); text-align: center; transform: rotate(2deg); }

  .badge { position: absolute; left: 339px; top: 574px; width: 180px; height: 180px; border-radius: 50%;
    background: var(--badge-red); display: flex; align-items: center; justify-content: center; }
  .badge-text { width: 140px; font-family: "Oswald", sans-serif; font-size: 18px; line-height: 1.15;
    color: var(--white); text-align: center; transform: rotate(8deg); }
</style>
</head>
<body>
<div class="canvas">
  <div class="cover">
    <section class="back-cover">
      <h2 class="back-title">Der Mutkompass</h2>
      <p class="back-blurb">Lorem ipsum dolor sit amet, consectetuer adipiscing elit. Aenean commodo ligula eget dolor. Aenean massa. Cum sociis natoque penatibus et magnis dis parturient montes, nascetur ridiculus mus. Donec quam felis, ultricies nec, pellentesque eu, pretium quis, sem. Nulla consequat massa quis enim. Donec pede justo, fringilla vel, aliquet nec, vulputate eget, arcu. In enim justo, rhoncus ut, imperdiet a, venenatis vitae, justo. Nullam dictum felis eu pede mollis pretium.</p>
    </section>

    <section class="spine">
      <div class="spine-text"><span class="spine-author">Name Autor</span><span class="spine-title">Der Mutkompass</span></div>
    </section>

    <section class="front-cover">
      <div class="photo-child" role="img" aria-label="Foto eines lachenden Jungen im gestreiften Shirt, der ein Pappschild über den Kopf hält"></div>
      <div class="front-author">Name Autor</div>
      <h1 class="front-title">
        <span class="title-row">
          <span class="title-small"><span>Der</span></span>
          <span class="title-big">Mut-</span>
        </span>
        <span class="title-big">Kompass</span>
      </h1>
      <div class="sign"><div class="sign-text">ELTERN-<br>RATGEBER</div></div>
      <div class="badge"><div class="badge-text">Sieben Schritte zu innerer Ruhe im Familienalltag mit Schulanfängern</div></div>
    </section>
  </div>
</div>
</body>
</html>
```